I need someone to design a flyer for my business website. I would like a designer to use my website information to create a flyer. You can view a preliminary example of the website at www.bluvantours.zaplinkhost.example, although the real website will go live in a few days at www.bluvan-tours.example.

*** Summarize the information on the website. DO NOT cut and past. The students will typically be on their way to class when they will see this flyer. This flyer must not only grab their attention, but also give the relevant information as concisely as possible.

*** Be sure to include the following: Name of company in bold on the flyer, website address (www.bluvan-tours.example), and the service we provide (coach transportation).
Updates

Project Deadline Extended
Reason: The Thanksgiving holiday made it difficult for many designers to submit their designs. Therefore, Bluvan Tours will be extending our deadline by 2 days. Please make sure to have your final designs in by this 3:24pm on November 29th.

Project Deadline Extended
Reason: Updated note in the brief: *** Please develop a unique summary for the information on the website (www.bluvantours.zaplinkhost.example). Do not copy and past the information. This will be the last extention! I am impressed with all of your submissions. Feel free to play around more with your advertisement to make it stand out to students. They are typically going to be on their way to class when they see this flyer, so they need the important information and only the important information! Best wishes, Bluvan Tours

I have attached a picture of the actual website that will appear at www.bluvan-tours.example. Try to make the flyer represent the website.

Great submissions so far from all of you! I'm quite impressed!

Target Market(s)

College Students! They will be rushing to their classes when they see this flyer.

Industry/Entity Type

Business

Requirements
Must have
• *** Be sure to include the following: Name of company in bold on the flyer, website address (www.bluvan-tours.example), and the service we provide (coach transportation).
Nice to have
• I have attached a picture of the actual website that will appear at www.bluvan-tours.example. Try to make the flyer represent the website.
Should not have
• *** Summarize the information on the website. DO NOT cut and past. The students will typically be on their way to class when they will see this flyer. This flyer must not only grab their attention, but also give the relevant information as concisely as possible.

```html
<!DOCTYPE html>
<html lang="en">
<head>
<meta charset="utf-8">
<title>Bluvan Tours – Ski Coach Flyer</title>
<link rel="stylesheet" href="https://fonts.googleapis.com/css2?family=Bebas+Neue&family=Josefin+Sans:wght@700&family=Oswald:wght@400;500&display=swap">
<style>
  :root {
    --ink: #4b1c2c;
    --cream: #e9f0d2;
    --snow-light: #dfeab8;
    --snow-mid: #a9c283;
    --snow-dark: #5f7a52;
    --forest: #3b2a32;
    --panel: rgba(205, 220, 170, 0.55);
  }
  html, body {
    margin: 0;
    padding: 0;
    overflow: hidden;
    background: #ffffff;
  }
  .flyer {
    position: relative;
    width: 872px;
    height: 1200px;
    overflow: hidden;
    color: var(--ink);
  }
  .snow-scene {
    position: absolute;
    inset: 0;
    background:
      radial-gradient(ellipse 38% 60% at 50% 10%, var(--snow-light) 0%, rgba(223,234,184,0) 70%),
      linear-gradient(90deg, var(--snow-dark) 0%, var(--snow-mid) 30%, var(--snow-light) 50%, var(--snow-mid) 70%, var(--snow-dark) 100%);
  }
  .snow-scene::before {
    content: "";
    position: absolute;
    inset: 0 0 auto 0;
    height: 260px;
    background:
      radial-gradient(ellipse 22% 100% at 0% 0%, var(--forest) 0%, rgba(59,42,50,0) 100%),
      radial-gradient(ellipse 22% 100% at 100% 0%, var(--forest) 0%, rgba(59,42,50,0) 100%);
  }
  .question {
    position: absolute;
    top: 328px;
    left: 0;
    width: 100%;
    margin: 0;
    text-align: center;
    font-family: "Bebas Neue", sans-serif;
    font-weight: 400;
    font-size: 46px;
    line-height: 53.5px;
    letter-spacing: 3.4px;
  }
  .rule {
    position: absolute;
    left: 30px;
    width: 806px;
    height: 3px;
    background: var(--ink);
  }
  .rule--top { top: 559px; }
  .rule--bottom { top: 1124px; }
  .lead {
    position: absolute;
    left: 0;
    width: 100%;
    margin: 0;
    text-align: center;
    font-family: "Josefin Sans", sans-serif;
    font-weight: 700;
    font-size: 50px;
    line-height: 1;
    letter-spacing: 3px;
  }
  .lead--then { top: 610px; }
  .lead--for-you { top: 854px; }
  .brand-banner {
    position: absolute;
    left: 42px;
    top: 683px;
    width: 790px;
    height: 124px;
    background: var(--ink);
    transform: rotate(-5deg);
    display: flex;
    align-items: center;
    justify-content: center;
  }
  .brand-name {
    margin: 0;
    color: var(--cream);
    font-family: "Josefin Sans", sans-serif;
    font-weight: 700;
    font-size: 92px;
    line-height: 1;
    padding-top: 12px;
    letter-spacing: 2px;
    white-space: nowrap;
  }
  .services-panel {
    position: absolute;
    left: 0;
    top: 960px;
    width: 100%;
    height: 240px;
    background: var(--panel);
  }
  .services-title {
    position: absolute;
    left: 48px;
    top: 994px;
    margin: 0;
    font-family: "Oswald", sans-serif;
    font-weight: 500;
    font-size: 30px;
    line-height: 1;
    letter-spacing: 1px;
    text-transform: uppercase;
  }
  .services-list {
    position: absolute;
    left: 28px;
    top: 1037px;
    margin: 0;
    padding: 0;
    list-style: none;
    font-family: "Oswald", sans-serif;
    font-weight: 400;
    font-size: 15.5px;
    line-height: 20.5px;
    letter-spacing: 0.9px;
    text-transform: uppercase;
  }
  .services-list li::before { content: "- "; }
  .web-address {
    position: absolute;
    right: 36px;
    top: 1150px;
    margin: 0;
    font-family: "Oswald", sans-serif;
    font-weight: 500;
    font-size: 22px;
    line-height: 1;
    letter-spacing: 2px;
    text-transform: uppercase;
  }
</style>
</head>
<body>
<main class="flyer">
  <div class="snow-scene" role="img" aria-label="Photograph of a snowy forest trail with long skier shadows stretching toward the viewer, tinted green"></div>

  <h2 class="question">Love skiing or snowboarding?<br>Are you looking for transportation<br>to and from the various ski parks<br>near Madison, Wisconsin?</h2>

  <div class="rule rule--top"></div>

  <p class="lead lead--then">Then</p>
  <div class="brand-banner">
    <h1 class="brand-name">BLUVAN TOURS</h1>
  </div>
  <p class="lead lead--for-you">Is for you!</p>

  <section class="services-panel" aria-hidden="true"></section>
  <h3 class="services-title">Use our services:</h3>
  <ul class="services-list">
    <li>Offers transportation to and from Ridgecrest Hollow and Pinebluff via a coach bus</li>
    <li>Unique experience on our buses (awesome prizes, help services)</li>
    <li>You can share your specific needs with us through our blog</li>
  </ul>

  <div class="rule rule--bottom"></div>
  <p class="web-address">www.bluvan-tours.example</p>
</main>
</body>
</html>
```